Packaging Design Project

THIS IS A PRODUCT THAT IS SOLD IN SMOKE SHOPS AND HEAD SHOPS IT IS CALLED GOLDEN MEADOW IT WILL BE SOLD IN A 2 DRAM BLUE BOTTLE WITH A SILVER CAP BELOW IN FILES IS A SAMPLE OF THE WORDING I NEED ON THE BOOTLE ALSO I NEED TO ADD SOMETHING LIKE POWERED BY KRATOM IS THE MAIN INGREDIENT
Updates
i uploade a picture of bootle thanks
Industry/Entity Type
Product
Look and feel
Each slider illustrates characteristics of the customer's brand and the style your logo design should communicate.

```html
<!DOCTYPE html>
<html lang="en">
<head>
<meta charset="utf-8">
<title>Golden Meadow – Liquid Mood Enhancer Label</title>
<link rel="stylesheet" href="https://fonts.googleapis.com/css2?family=Arimo:ital,wght@0,700;1,400&display=swap">
<style>
  :root {
    --forest-light: #eef5ea;
    --forest-pale: #cfe4c2;
    --forest-mid: #93c27a;
    --forest-deep: #4d8a3a;
    --mist: #f2f6f3;
    --water-light: #dfe8ed;
    --water: #b3c7d2;
    --leaf-light: #86b95c;
    --leaf-mid: #4f9236;
    --leaf-deep: #2c6420;
    --brand-gold: #e0aa00;
    --mark-gold: #f4b400;
    --tagline-orange: #c87f0a;
    --ingredient-navy: #14324a;
  }
  * { margin: 0; padding: 0; box-sizing: border-box; }
  html, body {
    width: 679px;
    height: 1200px;
    overflow: hidden;
    background: #ffffff;
  }
  .label {
    position: relative;
    width: 679px;
    height: 1200px;
    overflow: hidden;
    font-family: "Arimo", Arial, sans-serif;
  }
  .forest-backdrop {
    position: absolute;
    inset: 0;
    background:
      radial-gradient(ellipse 40% 30% at 50% 35%, rgba(255,255,255,0.9), rgba(255,255,255,0) 75%),
      radial-gradient(ellipse 30% 25% at 12% 18%, rgba(77,138,58,0.55), rgba(77,138,58,0) 80%),
      radial-gradient(ellipse 30% 25% at 88% 20%, rgba(77,138,58,0.55), rgba(77,138,58,0) 80%),
      radial-gradient(ellipse 25% 30% at 8% 55%, rgba(77,138,58,0.5), rgba(77,138,58,0) 80%),
      radial-gradient(ellipse 25% 30% at 92% 55%, rgba(77,138,58,0.5), rgba(77,138,58,0) 80%),
      linear-gradient(90deg, var(--forest-mid) 0%, var(--forest-pale) 28%, var(--forest-light) 50%, var(--forest-pale) 72%, var(--forest-mid) 100%);
  }
  .mist-band {
    position: absolute;
    left: 0; right: 0;
    top: 620px;
    height: 380px;
    background: linear-gradient(180deg, rgba(242,246,243,0) 0%, var(--mist) 50%, var(--mist) 75%, rgba(242,246,243,0) 100%);
  }
  .water-surface {
    position: absolute;
    left: 0; right: 0;
    top: 900px;
    bottom: 0;
    background: linear-gradient(180deg, rgba(223,232,237,0) 0%, var(--water-light) 25%, var(--water) 60%, var(--water) 100%);
  }
  .leaf-cluster {
    position: absolute;
    left: 0; right: 0;
    bottom: 0;
    height: 320px;
    background:
      radial-gradient(ellipse 34% 62% at 80% 78%, var(--leaf-light) 0%, var(--leaf-mid) 55%, rgba(79,146,54,0) 100%),
      radial-gradient(ellipse 24% 48% at 48% 88%, var(--leaf-light) 0%, var(--leaf-mid) 55%, rgba(79,146,54,0) 100%),
      radial-gradient(ellipse 26% 40% at 14% 98%, var(--leaf-mid) 0%, var(--leaf-deep) 60%, rgba(44,100,32,0) 100%);
  }
  .brand-mark {
    position: absolute;
    left: 268px;
    top: 240px;
    width: 150px;
    height: 150px;
    border-radius: 50%;
    background: var(--mark-gold);
  }
  .brand-name {
    position: absolute;
    left: 0; right: 0;
    top: 530px;
    text-align: center;
    font-weight: 700;
    font-size: 112px;
    line-height: 106px;
    color: var(--brand-gold);
    letter-spacing: 1px;
  }
  .tagline {
    position: absolute;
    left: 104px;
    top: 800px;
    font-style: italic;
    font-weight: 400;
    font-size: 45px;
    line-height: 50px;
    color: var(--tagline-orange);
    letter-spacing: 1px;
  }
  .ingredient-note {
    position: absolute;
    left: 72px;
    top: 1080px;
    font-weight: 700;
    font-size: 37px;
    line-height: 42px;
    color: var(--ingredient-navy);
    text-shadow: 0 0 6px rgba(255,255,255,0.9), 0 0 2px #ffffff;
  }
</style>
</head>
<body>
  <main class="label">
    <div class="forest-backdrop" role="img" aria-label="Misty green forest canopy photograph"></div>
    <div class="mist-band"></div>
    <div class="water-surface" role="img" aria-label="Rippling water surface with a falling droplet"></div>
    <div class="leaf-cluster" role="img" aria-label="Fresh green kratom leaves"></div>

    <div class="brand-mark" aria-hidden="true"></div>
    <h1 class="brand-name">GOLDEN<br>MEADOW</h1>
    <p class="tagline">LIQUID MOOD<br>ENHANCER</p>
    <p class="ingredient-note">POWERED<br>BY KRATOM</p>
  </main>
</body>
</html>
```